The Quiet Ascent Book Cover

Book Title:
The Quiet Ascent: Lessons of Insight From A Circle of Mentors to Guide You Toward a Fuller Journey

This book will offer the wisdom and philosophies of a variety of different coaches to allow future clients to get a taste of you and your style and prepare them to work with you!

A coach does not fix you. Or heal you. They coach you - offer thoughts to ponder, guidance, techniques to try. All to help you plays and succeed at the game of life.

Each coach has their own personality, training, experience, method and philosophy they bring to the table. The underlying purpose is to guide you through The Quiet Ascent, to become the person you desire and aspire to be. Different coaches for different folks, yet they all have their own unique wisdom and special sauce to share.

This book is a collection of just that. A tasting of the wisdom and philosophies of a variety of different coaches for you to experience.

Types of Coaches: Clarity, Dreams, Goals, Motivation, Mindset,  Subconscious, Beliefs, Behavior, Accountability, Life, Wellness, Love & Dating, Relationships, Sex, Business, Career,  Executive,  Personal Development,  Writing, Wellness, Fitness, Parenting,  Style, Spirituality, Public Speaking, Financial,  Time management, Weight Loss, Running, Self esteem,  Tarot, Astrology, Enneagram, Soul path/ Dharma, Skills, Performance,  Speaking / Communication, Leadership, Shadow Work, Acting, Sports, ANY & ALL

Target Market(s)

Males or females looking for guidance and words of wisdom from an expert coach - maybe to find one that resonates with them to work with further. Ages 16 and up. Any Gender. International. Looking to improve their life!

Industry/Entity Type

Self Development, Wellness, Coaching, Personal Growth, Fitness, Spirituality, Business, Relationships

Font styles to use
Serif
Script

Colors
0054AA
0677BA
7BADD7
CADEEF
E8F1F8
FFF300
FFF600
FEFA6F
FFFEC7
FFFEE8

Requirements
Must have
• I am looking for a visually appealing, unique cover that encompasses the breadth and depth of the transformation that people can go through and inspires them to want to grow and change even more. I love when elegant and classic simplicity is combined with some kind of twist that catches the eye and provokes thought. I love complimentary fonts, colors, design elements. You can visit my Veltrano Author Page - Dr. Marisol Penbury Aldane to see my titles to see what I have liked! But I am also excited to see where you can make my vision even better!!
Nice to have
• Front Cover - Image, Title and Subtitle, The Lark Publishing House, Spine - Title and Publishing House Logo, Back - Book Blurb, Authors Names, Info about Publishing House, ISBN Barcode
Should not have
• Anything too feminine or too masculine as I want to encourage coaches of all genders to participate.

```html
<!DOCTYPE html>
<html lang="en">
<head>
<meta charset="utf-8">
<title>The Quiet Ascent — Book Cover</title>
<link href="https://fonts.googleapis.com/css2?family=Roboto+Condensed:wght@500&family=Barlow+Condensed:wght@500&family=Mr+Dafoe&display=swap" rel="stylesheet">
<style>
  :root {
    --backdrop: #1b2928;
    --cover-deep: #0f2b2b;
    --cover-mid: #124744;
    --cover-glow: #1d6a64;
    --butterfly-tone: #2f8b8a;
    --title-cyan: #14e8d6;
    --script-white: #ffffff;
  }
  * { margin: 0; padding: 0; box-sizing: border-box; }
  html, body {
    width: 1200px;
    height: 1200px;
    overflow: hidden;
    background: var(--backdrop);
  }
  .stage {
    position: relative;
    width: 1200px;
    height: 1200px;
  }
  .book-cover {
    position: absolute;
    left: 291px;
    top: 133px;
    width: 618px;
    height: 926px;
    overflow: hidden;
    background: var(--cover-deep);
  }
  .cover-art {
    position: absolute;
    inset: 0;
    width: 100%;
    height: 100%;
  }
  .title {
    position: absolute;
    left: 35px;
    top: 300px;
    color: var(--title-cyan);
    font-family: "Roboto Condensed", "Arial Narrow", sans-serif;
    font-weight: 500;
    font-size: 110px;
    line-height: 96px;
    letter-spacing: -0.02em;
  }
  .title-line { display: block; }
  .title-script {
    position: absolute;
    left: 34px;
    top: 492px;
    color: var(--script-white);
    font-family: "Mr Dafoe", cursive;
    font-weight: 400;
    font-size: 196px;
    line-height: 1;
    letter-spacing: 0;
    white-space: nowrap;
  }
  .subtitle {
    position: absolute;
    left: 312px;
    top: 712px;
    width: 300px;
    color: var(--title-cyan);
    font-family: "Barlow Condensed", "Arial Narrow", sans-serif;
    font-weight: 500;
    font-size: 31px;
    line-height: 41.5px;
    letter-spacing: -0.01em;
  }
  .subtitle-line { display: block; white-space: nowrap; }
</style>
</head>
<body>
  <main class="stage">
    <section class="book-cover">
      <svg class="cover-art" viewBox="0 0 618 926" role="img" aria-label="Teal bokeh photograph with a turquoise butterfly in flight near the top right">
        <defs>
          <radialGradient id="coverGlow" cx="0.55" cy="0.35" r="0.8">
            <stop offset="0" stop-color="var(--cover-glow)"/>
            <stop offset="0.5" stop-color="var(--cover-mid)"/>
            <stop offset="1" stop-color="var(--cover-deep)"/>
          </radialGradient>
          <radialGradient id="butterflyTone" cx="0.5" cy="0.5" r="0.5">
            <stop offset="0" stop-color="var(--butterfly-tone)" stop-opacity="0.85"/>
            <stop offset="1" stop-color="var(--butterfly-tone)" stop-opacity="0"/>
          </radialGradient>
        </defs>
        <rect width="618" height="926" fill="url(#coverGlow)"/>
        <ellipse cx="380" cy="290" rx="150" ry="170" fill="url(#butterflyTone)"/>
      </svg>

      <h1 class="title">
        <span class="title-line">The</span>
        <span class="title-line">Quiet</span>
      </h1>
      <p class="title-script">Ascent</p>

      <p class="subtitle">
        <span class="subtitle-line">Lessons of Insight From</span>
        <span class="subtitle-line">A Circle of Mentors</span>
        <span class="subtitle-line">to Guide You Toward</span>
        <span class="subtitle-line">a Fuller Journey</span>
      </p>
    </section>
  </main>
</body>
</html>
```